Email footer project

We are looking for a standardised email footer that can be changed monthly for various project we are working on.
Please refer to EMAIL FOOTER BRIEF FOR ALL INFORMATION

We have uploaded some previous footers as a sample.

Target Market(s)

property, environmental

Industry/Entity Type

energy and property

Colors
00AB8E
00BBA5
67D7C9
C6EFE9
E9F9F6

Requirements
Must have
• company branding - leafmarker.co.uk.

```html
<!DOCTYPE html>
<html lang="en">
<head>
<meta charset="utf-8">
<title>Leaf Marker – Monthly Email Footers</title>
<link rel="stylesheet" href="https://fonts.googleapis.com/css2?family=Quicksand:wght@500;600;700&family=Source+Sans+3:wght@400&display=swap">
<style>
  :root {
    --page-bg: #ffffff;
    --label-ink: #3d3d3f;
    --brand-green: #4faf4a;
    --forest: #2a5c2e;
    --forest-light: #3f7a3f;
    --mist: #d9d9d9;
    --white: #ffffff;
    --ink: #111111;
  }
  * { box-sizing: border-box; margin: 0; padding: 0; }
  html, body { width: 1200px; height: 1000px; overflow: hidden; background: var(--page-bg); }
  .sheet { position: relative; width: 1200px; height: 1000px; }

  .month-label {
    position: absolute; left: 100px;
    font-family: "Source Sans 3", sans-serif; font-weight: 400;
    font-size: 26px; color: var(--label-ink); line-height: 1;
  }

  .footer-banner { position: absolute; left: 100px; width: 1000px; height: 125px; }
  .footer-banner svg { position: absolute; inset: 0; width: 1000px; height: 125px; }

  .banner-message {
    position: absolute; top: 0; height: 125px;
    display: flex; align-items: center;
    font-family: "Quicksand", sans-serif; font-weight: 600;
    color: var(--white); line-height: 1.18;
  }
  .banner-headline {
    position: absolute; left: 480px; top: 17px;
    font-family: "Quicksand", sans-serif; font-weight: 700;
    font-size: 43px; line-height: 46px; letter-spacing: 1px;
    color: var(--forest);
  }
  .banner-button {
    position: absolute; left: 787px; top: 37px; width: 180px; height: 52px;
    background: var(--white); border-radius: 12px;
    display: flex; align-items: center; justify-content: center;
    font-family: "Quicksand", sans-serif; font-weight: 700;
    font-size: 17px; letter-spacing: 1px; color: var(--ink);
  }
  .page-number {
    position: absolute; right: 10px; bottom: 12px;
    font-family: "Source Sans 3", sans-serif; font-size: 11px; color: var(--ink);
  }
</style>
</head>
<body>
<div class="sheet">

  <svg width="0" height="0" style="position:absolute">
    <defs>
      <linearGradient id="forest-glow" x1="0" y1="0" x2="1" y2="1">
        <stop offset="0" stop-color="#2a5c2e"/>
        <stop offset="0.55" stop-color="#2c5f30"/>
        <stop offset="0.8" stop-color="#3f7a3f"/>
        <stop offset="1" stop-color="#2e6a32"/>
      </linearGradient>
    </defs>
  </svg>

  <!-- March -->
  <p class="month-label" style="top:117px">March 2022</p>
  <div class="footer-banner" style="top:160px">
    <svg viewBox="0 0 1000 125">
      <rect width="1000" height="125" fill="var(--brand-green)"/>
      <polygon role="img" aria-label="Faint globe image over dark green" points="6,0 398,0 420,62.5 400,125 6,125 26,62.5" fill="url(#forest-glow)"/>
      <polygon points="420,0 742,0 764,62.5 745,125 423,125 442,62.5" fill="var(--mist)"/>
    </svg>
    <p class="banner-message" style="left:57px;font-size:18px;line-height:21px">Leaf Marker are running a webinar<br>as part of our webinar series on<br>MEES, EPCs and ESG</p>
    <p class="banner-headline">DELIVERING<br>NET ZERO</p>
    <span class="banner-button">REGISTER NOW</span>
  </div>

  <!-- April -->
  <p class="month-label" style="top:320px">April 2022</p>
  <div class="footer-banner" style="top:363px">
    <svg viewBox="0 0 1000 125">
      <rect width="1000" height="125" fill="var(--brand-green)"/>
      <polygon role="img" aria-label="Faint globe image over dark green" points="6,0 398,0 420,62.5 400,125 6,125 26,62.5" fill="url(#forest-glow)"/>
      <polygon points="420,0 742,0 764,62.5 745,125 423,125 442,62.5" fill="var(--mist)"/>
    </svg>
    <p class="banner-message" style="left:63px;font-size:24px;line-height:28px">Are you reading for EPC<br>legislation changes in<br>April 2023?</p>
    <p class="banner-headline">DELIVERING<br>NET ZERO</p>
    <span class="banner-button">LEARN MORE</span>
  </div>

  <!-- May -->
  <p class="month-label" style="top:517px">May 2022</p>
  <div class="footer-banner" style="top:555px">
    <svg viewBox="0 0 1000 125">
      <rect width="1000" height="125" fill="var(--brand-green)"/>
      <polygon role="img" aria-label="Faint globe image over dark green" points="6,0 398,0 420,62.5 400,125 6,125 26,62.5" fill="url(#forest-glow)"/>
      <polygon points="420,0 742,0 764,62.5 745,125 423,125 442,62.5" fill="var(--mist)"/>
    </svg>
    <p class="banner-message" style="left:53px;font-size:21px;line-height:26px">Leaf Marker have a maturity<br>model to map out your<br>EPC Compliance.</p>
    <p class="banner-headline">DELIVERING<br>NET ZERO</p>
    <span class="banner-button">LEARN MORE</span>
  </div>

  <!-- June -->
  <p class="month-label" style="top:723px">June 2022</p>
  <div class="footer-banner" style="top:762px">
    <svg viewBox="0 0 1000 125">
      <rect width="1000" height="125" fill="var(--brand-green)"/>
      <polygon role="img" aria-label="Faint globe image over dark green" points="6,0 398,0 420,62.5 400,125 6,125 26,62.5" fill="url(#forest-glow)"/>
      <polygon points="420,0 742,0 764,62.5 745,125 423,125 442,62.5" fill="var(--mist)"/>
    </svg>
    <p class="banner-message" style="left:62px;font-size:21px;line-height:25px">Leaf Marker are launching<br>phase 2 of our Digital EPC<br>analylsis platform</p>
    <p class="banner-headline">DELIVERING<br>NET ZERO</p>
    <span class="banner-button">LEARN MORE</span>
  </div>

  <span class="page-number">010</span>
</div>
</body>
</html>
```